Business Card Update, need to bring life to the card, two sided color

We need a new business card design, are moving and changing addresses and need a new look, we have the logos already attached but need a new style moving forward. Can incorporate the color of the logo (The Green) as well, maybe a solid back? We deal with safety products revolving around static electricity and safety lighting. Would like to keep same font in second logo as well.

Target Market(s)

Electrical Safety, Lighting

Contact Information for Business Card

Lars Whitcombe
Vice President
Office: 555-284-7316
Cell: 555-862-0457
lars@tkwhitcombe.com
www.tkwhitcombe.com
4700 West Cedar Boulevard
Suite #320
Roswell, GA 30412

Font styles to use
Serif
Sans Serif

Requirements
Must have
• Since 1918
Nice to have
• Could use the 100 Year Logo for back of card, would like the back of card to be the same green as logo.
Should not have
• No black cards please.

```html
<!DOCTYPE html>
<html lang="en">
<head>
<meta charset="utf-8">
<title>T.K. Whitcombe — Business Card</title>
<link href="https://fonts.googleapis.com/css2?family=Arimo:wght@400;700&display=swap" rel="stylesheet">
<style>
  :root {
    --bg: #a2f5d1;
    --white: #ffffff;
    --green: #009245;
    --green-dark: #00602f;
    --green-deep: #004d26;
  }
  html, body {
    margin: 0;
    padding: 0;
    width: 1200px;
    height: 1200px;
    overflow: hidden;
    background: var(--bg);
  }
  .stage { display: block; width: 1200px; height: 1200px; }
  .card-face { fill: var(--white); }
  .deco-dark { fill: var(--green-deep); }
  .deco-green { fill: var(--green); }
  .bar-dark { fill: var(--green-dark); }
  .bar-green { fill: var(--green); }
  .seal-ring { fill: var(--white); stroke: var(--green); }
  .brand-name, .brand-sub, .brand-since, .seal-name, .contact-text, .person-name, .person-title {
    font-family: "Arimo", Arial, sans-serif;
    font-weight: 700;
  }
  .brand-name, .brand-sub, .brand-since { fill: var(--white); }
  .brand-sub { letter-spacing: 3px; }
  .brand-since { letter-spacing: 2px; }
  .seal-name { fill: var(--green); }
  .person-name { font-size: 28px; fill: var(--green-dark); }
  .person-title { font-size: 18px; fill: var(--green); letter-spacing: 1px; }
  .contact-text { font-size: 18px; fill: var(--white); }
  .icon-line { fill: none; stroke: var(--white); stroke-width: 2; }
  .icon-fill { fill: var(--white); }
</style>
</head>
<body>
<svg class="stage" viewBox="0 0 1500 1500" xmlns="http://www.w3.org/2000/svg">
  <defs>
    <linearGradient id="nameBand" x1="0" y1="1" x2="1" y2="0">
      <stop offset="0" stop-color="#00401f"/>
      <stop offset="1" stop-color="#00a04a"/>
    </linearGradient>
    <linearGradient id="contactBand" x1="0" y1="0" x2="1" y2="1">
      <stop offset="0" stop-color="#00a04a"/>
      <stop offset="0.5" stop-color="#00602f"/>
      <stop offset="1" stop-color="#001a0b"/>
    </linearGradient>
    <linearGradient id="backTopBand" x1="0" y1="0" x2="1" y2="1">
      <stop offset="0" stop-color="#009245"/>
      <stop offset="0.55" stop-color="#00602f"/>
      <stop offset="1" stop-color="#001a0b"/>
    </linearGradient>
    <linearGradient id="backBottomBand" x1="0" y1="1" x2="1" y2="0">
      <stop offset="0" stop-color="#001a0b"/>
      <stop offset="0.45" stop-color="#00602f"/>
      <stop offset="1" stop-color="#009245"/>
    </linearGradient>
    <clipPath id="frontClip"><rect x="278" y="157" width="944" height="578" rx="46"/></clipPath>
    <clipPath id="backClip"><rect x="278" y="765" width="944" height="578" rx="46"/></clipPath>
    <filter id="cardShadow" x="-5%" y="-5%" width="110%" height="115%">
      <feDropShadow dx="0" dy="6" stdDeviation="4" flood-color="#000" flood-opacity="0.25"/>
    </filter>
  </defs>

  <!-- Front of card -->
  <g class="card card-front">
    <rect class="card-face" x="278" y="157" width="944" height="578" rx="46" filter="url(#cardShadow)"/>
    <g clip-path="url(#frontClip)">
      <path d="M470 222 H1080 V288 A60 60 0 0 1 1020 348 H470 Z" fill="url(#nameBand)"/>
      <text class="brand-name" x="803" y="278" font-size="50" text-anchor="middle">T.K. Whitcombe</text>
      <text class="brand-sub" x="803" y="304" font-size="20" text-anchor="middle">Manufacturing Company, Inc.</text>
      <text class="brand-since" x="803" y="331" font-size="16" text-anchor="middle">SINCE 1918</text>

      <circle class="deco-dark" cx="1168" cy="188" r="60"/>
      <circle class="deco-dark" cx="1158" cy="278" r="22"/>
      <circle class="deco-dark" cx="1113" cy="295" r="10"/>
      <circle class="deco-dark" cx="1210" cy="328" r="14"/>
      <circle class="deco-dark" cx="1084" cy="178" r="6"/>

      <rect class="bar-dark" x="1032" y="375" width="220" height="20" rx="10"/>
      <rect class="bar-dark" x="765" y="401" width="480" height="20" rx="10"/>
      <rect class="bar-dark" x="917" y="427" width="330" height="20" rx="10"/>

      <text class="person-name" x="560" y="400">Lars Whitcombe</text>
      <text class="person-title" x="560" y="426">Vice President</text>

      <path d="M697 490 H1222 V665 H777 A80 80 0 0 1 697 585 Z" fill="url(#contactBand)"/>

      <g class="contact-icon">
        <path class="icon-fill" d="M773 510 l4 -2 l4 6 l-3 3 q3 6 9 9 l3 -3 l6 4 l-2 4 q-14 0 -21 -21 z"/>
      </g>
      <text class="contact-text" x="809" y="524">Office: 555-284-7316</text>
      <g class="contact-icon">
        <rect class="icon-line" x="776" y="533" width="13" height="20" rx="2"/>
        <line class="icon-line" x1="779" y1="549" x2="786" y2="549"/>
      </g>
      <text class="contact-text" x="809" y="548">Cell: 555-862-0457</text>
      <g class="contact-icon">
        <rect class="icon-fill" x="771" y="559" width="23" height="15" rx="1"/>
        <path d="M772 560 L782.5 568 L793 560" fill="none" stroke="#00602f" stroke-width="2"/>
      </g>
      <text class="contact-text" x="809" y="572">lars@tkwhitcombe.com</text>
      <g class="contact-icon">
        <circle class="icon-line" cx="782" cy="590" r="10"/>
        <ellipse class="icon-line" cx="782" cy="590" rx="4.5" ry="10"/>
        <line class="icon-line" x1="772" y1="590" x2="792" y2="590"/>
      </g>
      <text class="contact-text" x="809" y="596">www.tkwhitcombe.com</text>
      <g class="contact-icon">
        <path class="icon-fill" d="M782 632 l-8 -12 a9 9 0 1 1 16 0 z"/>
        <circle cx="782" cy="615" r="3.5" fill="#00602f"/>
      </g>
      <text class="contact-text" x="809" y="620">4700 West Cedar Boulevard, Suite #320</text>
      <text class="contact-text" x="809" y="644">Roswell, GA 30412</text>

      <rect class="bar-green" x="464" y="507" width="20" height="260" rx="10"/>
      <rect class="bar-green" x="490" y="455" width="20" height="320" rx="10"/>
      <rect class="bar-green" x="516" y="577" width="20" height="200" rx="10"/>

      <circle class="deco-green" cx="333" cy="703" r="58"/>
      <circle class="deco-green" cx="343" cy="613" r="22"/>
      <circle class="deco-green" cx="290" cy="562" r="14"/>
      <circle class="deco-green" cx="387" cy="597" r="10"/>
      <circle class="deco-green" cx="416" cy="714" r="6"/>

      <circle class="seal-ring" cx="403" cy="287" r="124" stroke-width="12"/>
      <text class="seal-name" x="403" y="300" font-size="36" text-anchor="middle">Whitcombe</text>
    </g>
  </g>

  <!-- Back of card -->
  <g class="card card-back">
    <rect class="card-face" x="278" y="765" width="944" height="578" rx="46" filter="url(#cardShadow)"/>
    <g clip-path="url(#backClip)">
      <path d="M270 830 H907 V895 A60 60 0 0 1 847 955 H270 Z" fill="url(#backTopBand)"/>
      <path d="M700 1105 H1230 V1262 H780 A80 80 0 0 1 700 1182 Z" fill="url(#backBottomBand)"/>

      <circle class="deco-green" cx="1168" cy="796" r="60"/>
      <circle class="deco-green" cx="1158" cy="886" r="22"/>
      <circle class="deco-green" cx="1113" cy="903" r="10"/>
      <circle class="deco-green" cx="1210" cy="937" r="14"/>
      <circle class="deco-green" cx="1084" cy="786" r="6"/>

      <rect class="bar-green" x="1032" y="982" width="220" height="20" rx="10"/>
      <rect class="bar-green" x="880" y="1008" width="370" height="20" rx="10"/>
      <rect class="bar-green" x="917" y="1035" width="330" height="20" rx="10"/>

      <rect class="bar-green" x="464" y="1114" width="20" height="260" rx="10"/>
      <rect class="bar-green" x="490" y="1019" width="20" height="360" rx="10"/>
      <rect class="bar-green" x="516" y="1184" width="20" height="200" rx="10"/>

      <circle class="deco-green" cx="333" cy="1310" r="58"/>
      <circle class="deco-green" cx="343" cy="1221" r="22"/>
      <circle class="deco-green" cx="290" cy="1170" r="14"/>
      <circle class="deco-green" cx="387" cy="1204" r="10"/>
      <circle class="deco-green" cx="416" cy="1322" r="6"/>

      <circle class="seal-ring" cx="750" cy="1053" r="158" stroke-width="18"/>
      <text class="seal-name" x="750" y="1060" font-size="46" text-anchor="middle">Whitcombe</text>
      <text class="seal-name" x="750" y="1095" font-size="20" text-anchor="middle" letter-spacing="2">SINCE 1918</text>
    </g>
  </g>
</svg>
</body>
</html>
```